New Online Community needs a "Call To Action" Business Card!

I want to design a business card to be given to potential customers for my new online community called "Lease Nest Hub". I want the business card to have a QR code on it that leads back to a landing page and gives the user a 2 month free trial.

FRONT SIDE
[Logo]
Lease Nest Hub
Empowering Rental Property Owners

[QR Code]
Scan for a 2-month free trial!
Professional courses valued at
thousands of dollars included for free

Name : Dorian Pelkey
Title: President
Email: dorian.pelkey@leasenesthub.example
Direct Phone: 555-382-7140
Website: www.leasenesthub.example

BACK SIDE
Join a community of rental property
owners collaborating to manage rentals
successfully and build generational
wealth.

Key Highlights:
• Forums for questions and ideas
• Monthly live events
• LNH Academy courses valued at
thousands of dollars included for
free

Private, ad-free, and supportive
environment.

"Coming together is a beginning, staying together is progress, and working together is success." - Walter Brisco

Target Market(s)

Rental property owners that choose to manage their properties themselves

Industry/Entity Type

Real estate investing

Contact Information for Business Card

Two sided card, standard 2" x 3.5", main focus is the QR code to scan for the free 2 month trial. Boxes of these cards will be distributed to Realtors and other industry referral partners (mortgage brokers, insurance agents, real estate lawyers)

Requirements
Must have
• QR code, incorporate logo colours on the card, make the card very "fun" and engaging
Nice to have
• Modern, fun design.

```html
<!DOCTYPE html>
<html lang="en">
<head>
<meta charset="UTF-8">
<title>Lease Nest Hub – Business Card</title>
<link href="https://fonts.googleapis.com/css2?family=Figtree:wght@400;500;600;700;800&display=swap" rel="stylesheet">
<style>
  :root {
    --sheet: #ffffff;
    --navy: #02173a;
    --navy-soft: #0b2452;
    --ink: #0b1530;
    --sky: #0aa2f5;
    --orchid: #e46cf0;
    --violet: #a67cf5;
    --mist: #c9d3ee;
    --card-edge: #b9bccb;
  }
  * { margin: 0; padding: 0; box-sizing: border-box; }
  html, body {
    width: 1200px; height: 1200px; overflow: hidden;
    background: var(--sheet);
    font-family: "Figtree", sans-serif;
  }
  .sheet { position: relative; width: 1200px; height: 1200px; }

  .card {
    position: absolute; left: 160px; width: 745px; height: 419px; overflow: hidden;
  }
  .card--front { top: 125px; background: #fff; border: 1px solid var(--card-edge); }
  .card--back { top: 662px; background: var(--navy); color: #fff; }

  .side-label {
    position: absolute; left: 1007px;
    font-size: 30px; font-weight: 500; color: #000; letter-spacing: 0.5px;
  }
  .side-label--front { top: 328px; }
  .side-label--back { top: 850px; }

  /* front */
  .front-backdrop {
    position: absolute; inset: 0;
    background:
      radial-gradient(ellipse 60% 75% at 78% 55%, rgba(214,226,252,0.75), rgba(246,236,252,0.35) 60%, rgba(255,255,255,0) 85%),
      linear-gradient(120deg, #f4f7fe 0%, #fbf3fd 45%, #ffffff 70%);
  }
  .brand-mark { position: absolute; border-radius: 50%; background: var(--violet); }
  .card--front .brand-mark { left: 111px; top: 38px; width: 40px; height: 40px; }
  .front-brand {
    position: absolute; left: 59px; top: 88px;
    font-size: 14px; font-weight: 500; color: var(--ink); letter-spacing: 0.2px;
  }
  .front-tagline {
    position: absolute; left: 59px; top: 108px;
    font-size: 12px; font-weight: 600; color: var(--orchid);
  }
  .contact { position: absolute; left: 58px; top: 190px; color: var(--ink); }
  .contact__name { font-size: 21px; font-weight: 800; color: var(--sky); line-height: 26px; }
  .contact__title { font-size: 20px; font-weight: 700; color: var(--orchid); line-height: 26px; margin-bottom: 2px; }
  .contact__line { font-size: 16px; font-weight: 500; line-height: 21px; }

  .offer {
    position: absolute; left: 470px; top: 40px; width: 240px;
    text-align: center; color: var(--ink);
  }
  .offer__code {
    display: block; width: 170px; height: 170px; margin: 0 auto 14px;
    background: #fff; border-radius: 14px; border: 3px solid var(--violet);
  }
  .offer__cta { font-size: 18px; font-weight: 800; color: var(--sky); line-height: 22px; margin-bottom: 6px; }
  .offer__note { font-size: 13px; font-weight: 500; line-height: 17px; }

  /* back */
  .back-backdrop {
    position: absolute; left: 371px; top: 40px; width: 374px; height: 379px;
    background: radial-gradient(ellipse 70% 65% at 55% 50%, rgba(14,33,78,0.95), rgba(8,28,66,0.6) 55%, rgba(2,23,58,0) 85%);
  }
  .card--back .brand-mark { left: 220px; top: 30px; width: 36px; height: 36px; }
  .back-brand {
    position: absolute; left: 268px; top: 26px;
    font-size: 32px; font-weight: 700; color: #ffffff; letter-spacing: 1.5px; line-height: 42px;
  }
  .back-col { position: absolute; top: 98px; width: 320px; font-size: 13.5px; line-height: 19px; }
  .back-col--about { left: 38px; }
  .back-col--highlights { left: 388px; }
  .back-col p + p { margin-top: 12px; }
  .back-col__accent { color: var(--orchid); font-weight: 700; }
  .highlights__head { font-size: 15px; font-weight: 800; color: var(--sky); margin-bottom: 6px; }
  .highlights__list { list-style: none; }
  .highlights__list li { position: relative; padding-left: 16px; margin-bottom: 5px; }
  .highlights__list li::before {
    content: ""; position: absolute; left: 0; top: 6px;
    width: 7px; height: 7px; border-radius: 50%; background: var(--violet);
  }
  .back-quote {
    position: absolute; left: 38px; right: 38px; top: 318px;
    padding-top: 14px; border-top: 1px solid var(--navy-soft);
    font-size: 13.5px; line-height: 19px; color: var(--mist); text-align: center;
  }
  .back-quote__by { color: var(--orchid); font-weight: 700; }
</style>
</head>
<body>
<main class="sheet">
  <section class="card card--front">
    <div class="front-backdrop" role="img" aria-label="Soft lavender and sky-blue pattern backdrop"></div>
    <span class="brand-mark" aria-hidden="true"></span>
    <div class="front-brand">Lease Nest Hub</div>
    <div class="front-tagline">Empowering Rental Property Owners</div>
    <div class="contact">
      <p class="contact__name">Dorian Pelkey</p>
      <p class="contact__title">President</p>
      <p class="contact__line">dorian.pelkey@leasenesthub.example</p>
      <p class="contact__line">555-382-7140</p>
      <p class="contact__line">www.leasenesthub.example</p>
    </div>
    <div class="offer">
      <span class="offer__code" role="img" aria-label="QR code linking to the free trial landing page"></span>
      <p class="offer__cta">Scan for a 2-month free trial!</p>
      <p class="offer__note">Professional courses valued at thousands of dollars included for free</p>
    </div>
  </section>
  <p class="side-label side-label--front">FRONT</p>

  <section class="card card--back">
    <div class="back-backdrop" role="img" aria-label="Faint large navy brand decoration"></div>
    <span class="brand-mark" aria-hidden="true"></span>
    <div class="back-brand">Lease Nest Hub</div>
    <div class="back-col back-col--about">
      <p>Join a community of rental property owners collaborating to manage rentals successfully and build generational wealth.</p>
      <p class="back-col__accent">Private, ad-free, and supportive environment.</p>
    </div>
    <div class="back-col back-col--highlights">
      <p class="highlights__head">Key Highlights:</p>
      <ul class="highlights__list">
        <li>Forums for questions and ideas</li>
        <li>Monthly live events</li>
        <li>LNH Academy courses valued at thousands of dollars included for free</li>
      </ul>
    </div>
    <p class="back-quote">“Coming together is a beginning, staying together is progress, and working together is success.” <span class="back-quote__by">– Walter Brisco</span></p>
  </section>
  <p class="side-label side-label--back">BACK</p>
</main>
</body>
</html>
```